Existing graphics (3D cube) should be made more understandable

Hi,
I would like to make my 3D cube more understandable, but it should also be more presentable. I have attached a detailed description as an attachment. I think the image so far is good, but if we can improve it (more understandable and prettier), I would be happy.
BR
Tor

Target Market(s)

Students, Teachers, Prof.

Colors
0054AA
0677BA
7BADD7
CADEEF
E8F1F8
0094D4
00A9DD
6FCCEA
C7EBF8
E9F6FB
00AB8E
00BBA5
67D7C9
C6EFE9
E9F9F6
59FF00
82FF00
B8FF75
E3FFCB
F4FFEA

Requirements
Must have
• please see attachment
Nice to have
• please see attachment
Should not have
• please see attachment

```html
<!DOCTYPE html>
<html lang="de">
<head>
<meta charset="utf-8">
<title>Führungskräfte-Würfel</title>
<link rel="stylesheet" href="https://fonts.googleapis.com/css2?family=Figtree:wght@400;600;700;800&display=swap">
<style>
  :root {
    --ink: #15233a;
    --ink-soft: #2b3a52;
    --navy: #0054AA;
    --blue: #0677BA;
    --blue-mid: #7BADD7;
    --blue-light: #CADEEF;
    --blue-pale: #E8F1F8;
    --cyan: #0094D4;
    --cyan-mid: #6FCCEA;
    --cyan-light: #C7EBF8;
    --cyan-pale: #E9F6FB;
    --teal: #00AB8E;
    --teal-2: #00BBA5;
    --teal-mid: #67D7C9;
    --teal-light: #C6EFE9;
    --teal-pale: #E9F9F6;
    --neutral: #f1f3f6;
    --neutral-side: #e3e7ec;
    --edge: #ffffff;
    --bg: #ffffff;
  }
  html, body { margin: 0; padding: 0; overflow: hidden; background: var(--bg); }
  .canvas { width: 1200px; height: 840px; position: relative; overflow: hidden; }
  .diagram { display: block; width: 1200px; height: 840px; font-family: "Figtree", Arial, sans-serif; }
  .axis-title { font-size: 25px; fill: var(--ink); }
  .axis-title-x { fill: var(--teal); font-weight: 600; }
  .axis-title-y { fill: var(--navy); font-weight: 600; }
  .axis-title-z { fill: var(--ink-soft); }
  .scale-label { font-size: 17px; font-weight: 800; letter-spacing: 0.6px; fill: var(--ink); }
  .flex-label { font-size: 23px; font-weight: 700; fill: var(--cyan); }
  .cat-title { font-size: 18px; font-weight: 800; fill: var(--ink); }
  .cat-text { font-size: 18.5px; fill: var(--ink); }
  .marker { font-size: 30px; font-weight: 800; fill: var(--navy); }
  .marker-light { fill: #ffffff; }
  .cat-title-light, .cat-text-light { fill: #ffffff; }
  .face { stroke: var(--edge); stroke-width: 2.5; stroke-linejoin: round; }
  .axis-y { stroke: var(--navy); stroke-width: 3; fill: none; }
  .axis-x { stroke: var(--teal); stroke-width: 3; fill: none; }
  .axis-z { stroke: var(--cyan); stroke-width: 3; fill: none; }
  .head-y { fill: var(--navy); }
  .head-x { fill: var(--teal); }
  .head-z { fill: var(--cyan); }
  .depth-dash { stroke: var(--cyan); stroke-width: 2; stroke-dasharray: 8 6; fill: none; opacity: 0.7; }
  .tick { stroke: var(--ink); stroke-width: 2; }
</style>
</head>
<body>
<div class="canvas">
<svg class="diagram" viewBox="0 0 1560 1092" xmlns="http://www.w3.org/2000/svg">

  <!-- Cube faces -->
  <g class="cube">
    <!-- top row, top faces -->
    <polygon class="face" points="307,335 705,207 884,240 495,368" fill="var(--blue-light)"/>
    <polygon class="face" points="495,368 688,305 872,340 683,400" fill="var(--cyan-mid)"/>
    <polygon class="face" points="688,305 884,240 1080,272 872,340" fill="var(--teal-2)"/>
    <!-- top row, front & side faces -->
    <polygon class="face" points="307,335 495,368 495,603 307,570" fill="var(--blue-pale)"/>
    <polygon class="face" points="495,368 683,400 683,636 495,603" fill="var(--cyan-light)"/>
    <polygon class="face" points="683,400 872,340 872,573 683,636" fill="var(--cyan-mid)"/>
    <polygon class="face" points="872,340 1080,272 1080,507 872,573" fill="var(--teal)"/>
    <!-- bottom row -->
    <polygon class="face" points="307,570 495,603 495,838 307,806" fill="var(--neutral)"/>
    <polygon class="face" points="495,603 683,636 683,870 495,838" fill="var(--teal-light)"/>
    <polygon class="face" points="683,636 1080,507 1080,741 683,870" fill="var(--teal-pale)"/>
  </g>

  <!-- Axes -->
  <g class="axes">
    <line class="axis-y" x1="305" y1="806" x2="305" y2="196"/>
    <polygon class="head-y" points="305,180 295,202 315,202"/>
    <line class="tick" x1="297" y1="335" x2="313" y2="335"/>
    <line class="tick" x1="297" y1="570" x2="313" y2="570"/>

    <line class="axis-x" x1="305" y1="806" x2="838" y2="901"/>
    <polygon class="head-x" points="856,904 834,892 831,912"/>

    <line class="depth-dash" x1="307" y1="806" x2="1080" y2="549"/>
    <line class="axis-z" x1="1080" y1="549" x2="1136" y2="531"/>
    <polygon class="head-z" points="1152,526 1130,521 1136,541"/>
  </g>

  <!-- Axis titles -->
  <text class="axis-title axis-title-y" x="165" y="121">Exploration, Opening</text>
  <text class="axis-title axis-title-y" x="165" y="154">Leadership, Leader-Rolle</text>
  <text class="axis-title axis-title-x" x="778" y="952">Exploitation, Closing</text>
  <text class="axis-title axis-title-x" x="778" y="985">Leadership, Manager-Rolle</text>
  <g class="axis-title axis-title-z">
    <text x="1116" y="324">Flexibilität, um zwischen</text>
    <text x="1116" y="357">Exploration und</text>
    <text x="1116" y="389">Exploitation, Opening und</text>
    <text x="1116" y="422">Closing Leadership, Leader-</text>
    <text x="1116" y="455">und Manager-Rolle</text>
    <text x="1116" y="487">wechseln zu können</text>
  </g>

  <!-- Scale labels -->
  <text class="scale-label" x="221" y="343">STARK</text>
  <text class="scale-label" x="208" y="577">MITTEL</text>
  <text class="scale-label" x="186" y="813">SCHWACH</text>
  <text class="scale-label" x="452" y="870">MITTEL</text>
  <text class="scale-label" x="657" y="909">STARK</text>
  <text class="flex-label" x="227" y="855">Gering</text>
  <text class="flex-label" x="1139" y="564">Hoch</text>

  <!-- Categories -->
  <g text-anchor="middle">
    <text class="cat-title" x="399" y="433">KATEGORIE I:</text>
    <text class="cat-text" x="399" y="458">Führungskraft</text>
    <text class="cat-text" x="399" y="483">fürs Leadership</text>
    <text class="marker" x="390" y="536">• L</text>

    <text class="cat-title" x="592" y="441">KATEGORIE II:</text>
    <text class="cat-text" x="592" y="466">Führungskraft fürs</text>
    <text class="cat-text" x="592" y="491">Leadership und</text>
    <text class="cat-text" x="592" y="516">Management</text>
    <text class="marker" x="592" y="567">• LM</text>

    <text class="cat-title cat-title-light" x="976" y="363">KATEGORIE III:</text>
    <text class="cat-text cat-text-light" x="976" y="388">Führungskraft fürs</text>
    <text class="cat-text cat-text-light" x="976" y="413">Ambidextrous</text>
    <text class="cat-text cat-text-light" x="976" y="438">Leadership</text>
    <text class="marker marker-light" x="966" y="494">• A</text>

    <text class="cat-title" x="401" y="642">KATEGORIE V:</text>
    <text class="cat-text" x="401" y="667">Weder fürs</text>
    <text class="cat-text" x="401" y="692">Management noch</text>
    <text class="cat-text" x="401" y="716">Leadership</text>
    <text class="cat-text" x="401" y="741">geeignet</text>
    <text class="marker" x="398" y="784">• N</text>

    <text class="cat-title" x="589" y="697">KATEGORIE IV:</text>
    <text class="cat-text" x="589" y="722">Führungskraft fürs</text>
    <text class="cat-text" x="589" y="747">Management</text>
    <text class="marker" x="589" y="803">• M</text>
  </g>
</svg>
</div>
</body>
</html>
```